Expense Tracker App for Young Adults

I need a mobile app designer to design an app UI for me. It is for an expense tracker app. I’ve attached a mind map of the various screens and features of the app.

I would like to see designs for this app which is targeted towards young adults (late teens & early 20s) just starting their career who want to plan their budgets and track their expenses.
Updates

Hello designers! I'm conscious that this is not a guaranteed project, so I can understand that some of you might be apprehensive. Just wanted to let you know that I'm willing to see your initial drafts that show your direction and theme for design. You don't have to design the whole app. In fact, it's better if you share your initial design ideas so that we can have a discussion and I can give my input. If I see some good initial designs, I will be happy to make this a guaranteed project. I'm simply being cautious since I'm bootstrapping this and funding out of my own pocket. Thank you for your understanding!

Target Market(s)

Young adults who are just starting their careers, late teens and early 20s.

Font styles to use
Sans Serif

Requirements
Must have
• Ease of use, smart and sleek, a guided setup wizard which will help users setup their account after signing up.
Should not have
• Clunky

```html
<!DOCTYPE html>
<html lang="en">
<head>
<meta charset="utf-8">
<title>Expense Tracker App Design</title>
<link rel="stylesheet" href="https://fonts.googleapis.com/css2?family=Montserrat:wght@400;500;600;700&family=Poppins:wght@700&display=swap">
<style>
  :root {
    --stage: #1d1c1f;
    --purple-deep: #3f1f4f;
    --purple-mid: #55306a;
    --violet: #8e3fe0;
    --violet-soft: #c99cf0;
    --violet-pale: #ecdcf8;
    --ink: #2a2530;
    --muted: #8a8590;
    --line: #c9c5cc;
    --surface: #f5f4f6;
    --card: #ffffff;
    --expense: #e0424a;
    --badge: #e23b3b;
    --cafe: #2f9be0;
    --bills: #f3c530;
    --shop: #25b35a;
  }
  * { box-sizing: border-box; margin: 0; padding: 0; }
  html, body { width: 1200px; height: 1200px; overflow: hidden; background: var(--stage); }
  body { position: relative; font-family: "Montserrat", sans-serif; color: var(--ink); }

  .headline { position: absolute; left: 640px; top: 150px; font-family: "Poppins", sans-serif; font-weight: 700; font-size: 58px; line-height: 1.1; }
  .headline .line-1 { color: var(--violet); display: block; }
  .headline .line-2 { color: transparent; -webkit-text-stroke: 2px var(--violet); display: block; }

  .screen { position: absolute; left: 150px; top: 120px; width: 430px; height: 960px; background: var(--surface); border-radius: 46px; overflow: hidden; }

  .header { position: absolute; left: 0; top: 0; width: 100%; height: 300px; background: linear-gradient(160deg, var(--purple-mid), var(--purple-deep)); }
  .status { position: absolute; top: 18px; left: 34px; right: 30px; display: flex; justify-content: space-between; color: #fff; font-weight: 600; font-size: 16px; }
  .status-icons { display: flex; gap: 6px; align-items: center; }
  .greeting { position: absolute; left: 30px; top: 70px; display: flex; align-items: center; gap: 14px; color: #fff; }
  .avatar { width: 52px; height: 52px; border-radius: 50%; background: linear-gradient(135deg, #3f8ad8, #e9b9a0); border: 2px solid #fff; }
  .greeting small { display: block; font-size: 10px; letter-spacing: 1px; font-weight: 500; opacity: .85; }
  .greeting strong { font-size: 22px; font-weight: 700; }
  .header-actions { position: absolute; right: 28px; top: 78px; display: flex; gap: 22px; }
  .bell { position: relative; }
  .badge { position: absolute; top: -8px; right: -8px; width: 18px; height: 18px; border-radius: 50%; background: var(--badge); color: #fff; font-size: 10px; font-weight: 700; display: flex; align-items: center; justify-content: center; }

  .balance-card { position: absolute; left: 20px; top: 150px; width: 390px; height: 130px; background: var(--card); border-radius: 18px; overflow: hidden; box-shadow: 0 10px 24px rgba(0,0,0,.18); }
  .balance-card .label { position: absolute; left: 28px; top: 40px; font-size: 12px; letter-spacing: 1px; color: var(--muted); }
  .balance-card .amount { position: absolute; left: 28px; top: 62px; font-size: 32px; font-weight: 700; }
  .ring { position: absolute; border-radius: 50%; }
  .ring-3 { width: 190px; height: 190px; right: -50px; top: -95px; background: var(--violet-pale); }
  .ring-2 { width: 140px; height: 140px; right: -25px; top: -70px; background: var(--violet-soft); }
  .ring-1 { width: 96px; height: 96px; right: -3px; top: -48px; background: var(--violet); display: flex; align-items: flex-end; justify-content: center; padding-bottom: 12px; }

  .tabs { position: absolute; top: 310px; left: 0; width: 100%; display: flex; justify-content: space-around; font-size: 16px; font-weight: 500; }
  .tab.active { color: var(--violet); border-bottom: 3px solid var(--violet); padding-bottom: 8px; }

  .day { position: absolute; left: 20px; width: 390px; background: var(--card); border-radius: 18px; padding: 22px 24px 14px 24px; }
  .day-head { display: flex; align-items: center; gap: 14px; padding-bottom: 12px; border-bottom: 2px dotted var(--line); }
  .day-num { width: 46px; height: 46px; border-radius: 12px; background: var(--surface); display: flex; align-items: center; justify-content: center; font-size: 22px; font-weight: 700; }
  .day-meta small { display: block; font-size: 10px; letter-spacing: 1px; color: var(--muted); }
  .day-meta span { font-size: 16px; font-weight: 500; }
  .total, .price { margin-left: auto; color: var(--expense); font-weight: 700; }
  .total { font-size: 20px; }
  .item { display: flex; align-items: center; gap: 16px; padding: 12px 0; }
  .item-icon { width: 48px; height: 48px; border-radius: 50%; display: flex; align-items: center; justify-content: center; }
  .item strong { display: block; font-size: 16px; font-weight: 600; }
  .item em { font-style: normal; font-size: 11px; color: var(--muted); }
  .price { font-size: 16px; font-weight: 600; }

  .nav { position: absolute; bottom: 0; left: 0; width: 100%; height: 86px; background: var(--card); display: flex; justify-content: space-around; align-items: center; box-shadow: 0 -6px 18px rgba(0,0,0,.06); }
  .nav-item.active { border-top: 3px solid var(--violet); padding-top: 10px; margin-top: -13px; }
  .fab { width: 62px; height: 62px; border-radius: 50%; background: var(--violet); margin-top: -34px; display: flex; align-items: center; justify-content: center; box-shadow: 0 8px 18px rgba(142,63,224,.45); }
  .home-bar { position: absolute; bottom: 8px; left: 145px; width: 140px; height: 5px; border-radius: 3px; background: #111; }
</style>
</head>
<body>
  <h1 class="headline"><span class="line-1">Expense Tracker</span><span class="line-2">App Design</span></h1>

  <main class="screen">
    <section class="header">
      <div class="status">
        <span>9:41</span>
        <span class="status-icons">
          <svg width="18" height="12" viewBox="0 0 18 12"><rect x="0" y="8" width="3" height="4" fill="#fff"/><rect x="5" y="5" width="3" height="7" fill="#fff"/><rect x="10" y="2" width="3" height="10" fill="#fff"/><rect x="15" y="0" width="3" height="12" fill="#fff" opacity=".5"/></svg>
          <svg width="16" height="12" viewBox="0 0 16 12"><path d="M1 4a10 10 0 0 1 14 0M3.5 6.5a6.5 6.5 0 0 1 9 0M6 9a3 3 0 0 1 4 0" stroke="#fff" stroke-width="1.6" fill="none"/></svg>
          <svg width="26" height="12" viewBox="0 0 26 12"><rect x=".5" y=".5" width="22" height="11" rx="3" stroke="#fff" fill="none"/><rect x="2.5" y="2.5" width="18" height="7" rx="1.5" fill="#fff"/><rect x="23.5" y="4" width="2" height="4" fill="#fff"/></svg>
        </span>
      </div>
      <div class="greeting">
        <div class="avatar" role="img" aria-label="Profile photo of the user"></div>
        <div><small>GOOD MORNING</small><strong>Marco</strong></div>
      </div>
      <div class="header-actions">
        <span class="bell">
          <svg width="24" height="24" viewBox="0 0 24 24" fill="none" stroke="#fff" stroke-width="1.8"><path d="M6 17V11a6 6 0 0 1 12 0v6l2 2H4z"/><path d="M10 21h4"/></svg>
          <span class="badge">8</span>
        </span>
        <svg width="24" height="24" viewBox="0 0 24 24" fill="none" stroke="#fff" stroke-width="1.8" stroke-linejoin="round"><path d="M3 4h18l-7 8v7l-4 2v-9z"/></svg>
      </div>
      <div class="balance-card">
        <div class="ring ring-3"></div><div class="ring ring-2"></div>
        <div class="ring ring-1">
          <svg width="30" height="30" viewBox="0 0 30 30" fill="#fff"><path d="M11 6h8l-2 4h-4z"/><path d="M8 24c0-7 3-12 7-12s7 5 7 12a2 2 0 0 1-2 2H10a2 2 0 0 1-2-2z"/><text x="15" y="23" font-size="9" font-weight="700" text-anchor="middle" fill="#8e3fe0" font-family="Montserrat, sans-serif">$</text></svg>
        </div>
        <span class="label">CURRENT BALANCE</span>
        <span class="amount">$1,450.00</span>
      </div>
    </section>

    <nav class="tabs">
      <span class="tab">Last Month</span>
      <span class="tab active">This Month</span>
      <span class="tab">Future</span>
    </nav>

    <article class="day" style="top:360px;">
      <div class="day-head">
        <span class="day-num">18</span>
        <div class="day-meta"><small>TODAY</small><span>September 2020</span></div>
        <span class="total">-120.00</span>
      </div>
      <div class="item">
        <span class="item-icon" style="background:var(--cafe)"><svg width="24" height="24" viewBox="0 0 24 24" fill="none" stroke="#fff" stroke-width="2"><path d="M4 9h12v6a5 5 0 0 1-5 5H9a5 5 0 0 1-5-5z"/><path d="M16 11h2a2 2 0 0 1 0 4h-2"/><path d="M8 3v3M12 3v3"/></svg></span>
        <div><strong>Café</strong><em>Large coffee &amp; 1 sliced cake</em></div>
        <span class="price">-20.00</span>
      </div>
      <div class="item">
        <span class="item-icon" style="background:var(--bills)"><svg width="24" height="24" viewBox="0 0 24 24" fill="none" stroke="#fff" stroke-width="2"><rect x="5" y="3" width="14" height="18" rx="2"/><path d="M9 8h6M9 12h6M9 16h3"/></svg></span>
        <div><strong>Bills</strong><em>Internet</em></div>
        <span class="price">-100.00</span>
      </div>
    </article>

    <article class="day" style="top:625px;">
      <div class="day-head">
        <span class="day-num">17</span>
        <div class="day-meta"><small>YESTERDAY</small><span>September 2020</span></div>
        <span class="total">-250.00</span>
      </div>
      <div class="item">
        <span class="item-icon" style="background:var(--shop)"><svg width="24" height="24" viewBox="0 0 24 24" fill="none" stroke="#fff" stroke-width="2"><rect x="4" y="6" width="16" height="14" rx="2"/><path d="M9 6a3 3 0 0 1 6 0"/><path d="M9 12a3 3 0 0 0 6 0"/></svg></span>
        <div><strong>Shopping</strong><em>1 pair of shoes</em></div>
        <span class="price">-250.00</span>
      </div>
    </article>

    <article class="day" style="top:805px;">
      <div class="day-head">
        <span class="day-num">16</span>
        <div class="day-meta"><small>WEDNESDAY</small><span>September 2020</span></div>
        <span class="total">-80.00</span>
      </div>
    </article>

    <nav class="nav">
      <span class="nav-item active"><svg width="28" height="28" viewBox="0 0 24 24" fill="none" stroke="var(--violet)" stroke-width="1.8"><rect x="3" y="7" width="18" height="13" rx="2"/><path d="M6 7l9-4 2 4"/><circle cx="16" cy="13.5" r="1.3"/></svg></span>
      <span class="nav-item"><svg width="28" height="28" viewBox="0 0 24 24" fill="none" stroke="var(--ink)" stroke-width="1.8"><circle cx="12" cy="12" r="9"/><path d="M12 3v9l6.5 6"/></svg></span>
      <span class="fab"><svg width="24" height="24" viewBox="0 0 24 24" stroke="#fff" stroke-width="2.4" stroke-linecap="round"><path d="M12 5v14M5 12h14"/></svg></span>
      <span class="nav-item"><svg width="28" height="28" viewBox="0 0 24 24" fill="none" stroke="var(--ink)" stroke-width="1.8"><circle cx="12" cy="12" r="9"/><circle cx="12" cy="12" r="5"/><circle cx="12" cy="12" r="1.5"/></svg></span>
      <span class="nav-item"><svg width="28" height="28" viewBox="0 0 24 24" fill="none" stroke="var(--ink)" stroke-width="1.8"><rect x="3" y="3" width="7" height="7" rx="1"/><rect x="14" y="3" width="7" height="7" rx="1"/><rect x="3" y="14" width="7" height="7" rx="1"/><rect x="14" y="14" width="7" height="7" rx="1"/></svg></span>
      <span class="home-bar"></span>
    </nav>
  </main>
</body>
</html>
```